Meal Plan Website Needs New Pages Designed

Harvest Table Menus is an online, membership based program that delivers weekly meal programs (7 days worth of recipes plus shopping lists) carefully crafted by an expert team of meal planners. All recipes are created to comply with the following macronutrient ratio: 65% healthy fats, 25% lean protein, 10% good carbs.
All recipes are Paleo friendly and a great resource for those individuals who want to correctly implement this type of diet.

We are re-designing our website and need the following pages designed:

· Home page w/ logo
· How it works page
· Get Started! page
· Recipes Page template (these will be the pages on our site that will have recipes)
· Kitchen Essentials Training page (this will be a page with videos and tips + tricks, PDFs, etc)

So 5 total PSDs, 1 for each page.

Target audience: Men and women between the ages of 30 and 60 who want to:
· Eat healthy
· Lose weight
· Follow/Implement the Paleo diet
· Take the guesswork out of preparing delicious AND healthy meals for them and their families
· Know exactly what to eat, what to buy, how to make it

Feelings/Messages we want to communicate through the design:
· “Organic” but elegant look
· Fresh/light/Airy
· Simple but NOT GENERIC
· “I want to get cooking” feeling

Our Stylistic preferences:
· Minimalist with a few bold elements (something in between)
· Easy to visually navigate (enough white space, but not too much)
· There is more to “see” than to “read”

Our Color Preferences:
· Lighter pallet
· Colors that evoke natural woods, granite countertops…
· Stay away from using all dark colors

Our Font Type Preferences:
· Easy to read
· Not more than 3 font types
· Not too rigid
· Not too sophisticated
· Simple with a touch

Examples of Website Designs that we like:
· http://www.brightbasket41.example/menu-kits/
· http://stonehearth.example/
· https://www.wildforage.example/

```html
<!DOCTYPE html>
<html lang="en">
<head>
<meta charset="utf-8">
<title>Harvest Table Menus</title>
<link rel="stylesheet" href="https://fonts.googleapis.com/css2?family=Merriweather:wght@300;400&family=Arimo:wght@400;700&family=Roboto:wght@300;500&display=swap">
<style>
:root{
  --red:#e3141f;
  --orange:#f0582f;
  --brown:#5a2a1c;
  --ink:#3a3a3a;
  --muted:#8a8a8a;
  --soft:#9a9a9a;
  --band:#e4e4e4;
  --white:#fff;
  --black:#000;
}
*{box-sizing:border-box;margin:0;padding:0}
html,body{width:754px;height:1200px;overflow:hidden;background:var(--white)}
body{font-family:"Arimo",Arial,sans-serif;color:var(--ink)}
.page{position:relative;width:754px;height:1200px;overflow:hidden}
.abs{position:absolute}
.serif{font-family:"Merriweather",Georgia,serif}

/* header */
.topbar{left:0;top:0;width:754px;height:50px;background:var(--white)}
.navband{left:0;top:50px;width:754px;height:51px;background:linear-gradient(#f4f4f4,#dcdcdc);border-top:2px solid var(--red)}
.logo-bump{left:270px;top:40px}
.account-tab{top:0;width:29px;height:30px;font:700 6px/7px "Arimo",sans-serif;color:var(--white);text-align:center;padding-top:5px;clip-path:polygon(0 0,100% 0,100% 100%,50% 80%,0 100%)}
.tab-signin{left:114px;background:#b5b5b5}
.tab-join{left:143px;background:var(--red)}
.brand{left:200px;top:22px;width:354px;text-align:center;font:400 19px/1 "Merriweather",serif;color:var(--ink)}
.social-dot{top:14px;width:20px;height:20px;border-radius:50%;background:#a9a9a9;border:2px solid #d0d0d0}
.nav{left:0;top:72px;width:754px;display:flex;justify-content:center;align-items:center;gap:9px;font:400 7px/1 "Merriweather",serif;color:#555;text-transform:uppercase}
.nav .sep{color:#777}
.nav .active{background:var(--red);color:var(--white);padding:3px 5px;border-radius:3px}

/* hero */
.hero-photo{left:0;top:101px;width:754px;height:157px;background:linear-gradient(90deg,#6b3a2a 0%,#8a4a36 40%,#b06a4e 55%,#c9523a 70%,#a86448 100%)}
.hero-shade{left:0;top:101px;width:320px;height:157px;background:rgba(30,20,15,.55)}
.hero-title{left:124px;top:122px;width:190px;font:300 17px/21px "Roboto",sans-serif;color:var(--white);letter-spacing:-.3px}
.hero-title b{font-weight:500;color:var(--red)}
.hero-btn{left:123px;top:213px;width:117px;height:22px;background:var(--orange);border:1px solid #ff8a66;border-radius:2px;font:700 6.5px/20px "Arimo",sans-serif;color:var(--white);text-align:center;letter-spacing:.3px}

/* intro */
.headline{left:114px;top:272px;width:526px;text-align:center;font:300 19px/22px "Merriweather",serif;color:var(--soft);text-transform:uppercase}
.diet-list{left:114px;top:326px;width:526px;display:flex;justify-content:center;gap:9px;font:400 7px/1 "Arimo",sans-serif;color:#222}
.rule{left:114px;top:349px;width:526px;height:1px;background:#555}

/* plan cards */
.card{top:372px;width:159px}
.card-photo{height:110px;border:1px solid #c8c8c8}
.card-text{margin-top:11px;font:400 6.2px/9px "Arimo",sans-serif;color:var(--muted);text-align:justify}
.ribbon{display:inline-block;margin-top:9px;background:var(--orange);color:var(--white);font:700 6.2px/12px "Arimo",sans-serif;padding:0 10px 0 5px;clip-path:polygon(0 0,100% 0,92% 50%,100% 100%,0 100%)}
.pager{left:344px;top:571px}

/* features */
.feature-band{left:0;top:646px;width:754px;height:340px;background:linear-gradient(#fff 0%,#f0f0f0 40%,#d9d9d9 100%);border-top:3px solid var(--brown)}
.panel{top:652px;width:158px;height:258px;background:var(--white);border:1px solid #dcdcdc;box-shadow:0 6px 6px -4px rgba(0,0,0,.25)}
.badge{top:606px;width:80px;height:80px;border-radius:50%;background:var(--red);border:3px solid var(--brown);box-shadow:0 0 0 3px var(--white);display:flex;align-items:center;justify-content:center;text-align:center;font:400 12.5px/13px "Merriweather",serif;color:var(--white);text-transform:uppercase;letter-spacing:-.5px}
.meal-row{left:122px;display:flex;gap:8px;align-items:center;width:148px}
.meal-thumb{flex:0 0 38px;height:38px;border-radius:50%;border:2px solid #ddd;background:radial-gradient(circle,#c4553b,#8a5a3c)}
.meal-text{font:400 6.2px/8.5px "Arimo",sans-serif;color:var(--muted)}
.panel-photo{border:1px solid #c8c8c8}
.panel-text{left:306px;top:829px;width:141px;font:400 6.2px/8.3px "Arimo",sans-serif;color:var(--muted);text-align:justify}
.tips{left:488px;top:700px;list-style:none;font:300 12.5px/18px "Merriweather",serif;color:#333;text-transform:uppercase;letter-spacing:-.4px}
.tips li::before{content:"•";font-size:8px;margin-right:9px;vertical-align:middle}
.view-btn{top:884px;width:59px;height:13px;background:var(--orange);border-radius:2px;color:var(--white);font:700 6.2px/13px "Arimo",sans-serif;text-align:center}

/* newsletter & follow */
.section-label{font:400 11.5px/1 "Merriweather",serif;color:#555;text-transform:uppercase}
.email-field{left:114px;top:946px;width:172px;height:18px;background:var(--white);border:1px solid #ccc;font:400 6.5px/16px "Arimo",sans-serif;color:#777;padding-left:9px}
.submit-btn{left:286px;top:946px;width:82px;height:18px;background:var(--orange);color:var(--white);font:700 7px/18px "Arimo",sans-serif;text-align:center}
.follow-row{left:385px;top:960px;display:flex;align-items:center;gap:4px;font:400 4.5px/1 "Arimo",sans-serif;color:#555}
.ring{width:10px;height:10px;border-radius:50%;border:1px solid var(--orange)}
.chip{height:8px;padding:0 3px;border:1px solid #bbb;border-radius:2px;background:#fff;line-height:7px}
.chip.dark{background:#5b8fcf;color:#fff;border-color:#5b8fcf}
.sq{width:7px;height:7px;background:var(--orange);border-radius:1px}
.gap{width:10px}

/* footer */
.footer{left:0;top:986px;width:754px;height:214px;background:var(--black)}
.foot-col{top:1014px}
.foot-col h3{font:400 11.5px/1 "Merriweather",serif;color:var(--white);text-transform:uppercase;padding-bottom:7px;border-bottom:1px solid #555}
.foot-col.contact h3{color:var(--orange);border-color:var(--orange)}
.foot-col ul{list-style:none;margin-top:9px;font:400 6.2px/11px "Arimo",sans-serif;color:#777}
.foot-icon{top:1048px;width:14px;height:14px;border-radius:2px;background:var(--orange)}
.foot-brand{left:114px;top:1141px;font:400 14px/1 "Merriweather",serif;color:var(--white)}
.copyright{left:380px;top:1147px;width:260px;text-align:right;font:400 6px/1 "Arimo",sans-serif;color:#ddd}
</style>
</head>
<body>
<div class="page">

  <!-- header -->
  <div class="abs topbar"></div>
  <div class="abs navband"></div>
  <svg class="abs logo-bump" width="214" height="26" viewBox="0 0 214 26" aria-hidden="true">
    <path d="M0 10 H214 Q160 26 107 26 Q54 26 0 10 Z" fill="#fff"/>
  </svg>
  <div class="abs account-tab tab-signin">SIGN<br>IN</div>
  <div class="abs account-tab tab-join">JOIN<br>NOW</div>
  <div class="abs brand">Harvest Table Menus</div>
  <div class="abs social-dot" style="left:549px"></div>
  <div class="abs social-dot" style="left:573px"></div>
  <div class="abs social-dot" style="left:596px"></div>
  <div class="abs social-dot" style="left:620px"></div>

  <nav class="abs nav">
    <span class="active">Home</span><span class="sep">·</span>
    <span>How it work</span><span class="sep">·</span>
    <span>Get started</span><span class="sep">·</span>
    <span>Recipes</span><span class="sep">·</span>
    <span>Kitchen essential</span><span class="sep">·</span>
    <span>FAQ's</span><span class="sep">·</span>
    <span>Contact us</span>
  </nav>

  <!-- hero -->
  <div class="abs hero-photo" role="img" aria-label="Photo of peppers, tomatoes, garlic, pasta, cheese and olive oil on a terracotta surface"></div>
  <div class="abs hero-shade"></div>
  <h1 class="abs hero-title">Welcome to <b>Harvest Table Menus</b> - Hundreds of Delicious Meal Recipes...</h1>
  <div class="abs hero-btn">ACCESS THE PALEO RECIPES</div>

  <!-- intro -->
  <h2 class="abs headline">20 Ingredients a week for<br>health and happiness</h2>
  <div class="abs diet-list">
    <span>Classic</span><span>•</span><span>Vegetarian</span><span>•</span><span>Gluten Free</span><span>•</span><span>Dairy Free</span><span>•</span><span>Kosher</span><span>•</span><span>For one</span><span>•</span><span>Lunch</span>
  </div>
  <div class="abs rule"></div>

  <div class="abs card" style="left:114px">
    <div class="card-photo" role="img" aria-label="Classic plan: tomato and mozzarella salad with basil, titled Classic" style="background:linear-gradient(135deg,#f4f1ec,#e0704e 55%,#f2ede6)"></div>
    <p class="card-text">Lorem Ipsum has been the industry's standard dummy text ever since the 1500s, when an unknown printer took a galley of type and scrambled it to make a type specimen book.</p>
    <span class="ribbon">LEARN MORE</span>
  </div>
  <div class="abs card" style="left:297px">
    <div class="card-photo" role="img" aria-label="Vegetarian plan: rice with stir-fried vegetables, titled Vegetarian" style="background:linear-gradient(135deg,#e87a3a,#e9dcc4 50%,#3d5b86)"></div>
    <p class="card-text">Lorem Ipsum has been the industry's standard dummy text ever since the 1500s, when an unknown printer took a galley of type and scrambled it to make a type specimen book.</p>
    <span class="ribbon">LEARN MORE</span>
  </div>
  <div class="abs card" style="left:480px">
    <div class="card-photo" role="img" aria-label="Gluten free plan: bread over a bowl of stew, titled Gluten Free" style="background:linear-gradient(160deg,#5a4a3a,#c8a27a 45%,#6a3a20)"></div>
    <p class="card-text">Lorem Ipsum has been the industry's standard dummy text ever since the 1500s, when an unknown printer took a galley of type and scrambled it to make a type specimen book.</p>
    <span class="ribbon">LEARN MORE</span>
  </div>

  <svg class="abs pager" width="66" height="12" viewBox="0 0 66 12" aria-label="Slide navigation">
    <path d="M5 2 L1 6 L5 10" fill="none" stroke="#888" stroke-width="1.2"/>
    <circle cx="19" cy="6" r="4" fill="#aaa"/>
    <circle cx="28" cy="6" r="3.4" fill="#fff" stroke="#aaa" stroke-width="1.2"/>
    <circle cx="37" cy="6" r="4" fill="#aaa"/>
    <circle cx="46" cy="6" r="4" fill="#aaa"/>
    <path d="M61 2 L65 6 L61 10" fill="none" stroke="#888" stroke-width="1.2"/>
  </svg>

  <!-- features -->
  <div class="abs feature-band"></div>

  <div class="abs panel" style="left:116px"></div>
  <div class="abs panel" style="left:298px"></div>
  <div class="abs panel" style="left:480px"></div>

  <div class="abs badge" style="left:154px">This<br>week<br>meals</div>
  <div class="abs badge" style="left:337px">How is<br>work</div>
  <div class="abs badge" style="left:519px">Tips &amp;<br>tricks</div>

  <div class="abs meal-row" style="top:701px"><div class="meal-thumb" role="img" aria-label="Grilled steak with vegetables"></div><p class="meal-text">Lorem Ipsum is simply dummy text of the printing and typesetting industry.</p></div>
  <div class="abs meal-row" style="top:745px"><div class="meal-thumb" role="img" aria-label="Toasted sandwich" style="background:radial-gradient(circle,#d9b27a,#8a6240)"></div><p class="meal-text">Lorem Ipsum is simply dummy text of the printing and typesetting industry.</p></div>
  <div class="abs meal-row" style="top:790px"><div class="meal-thumb" role="img" aria-label="Mushrooms and garlic" style="background:radial-gradient(circle,#f1ece4,#b59a7a)"></div><p class="meal-text">Lorem Ipsum is simply dummy text of the printing and typesetting industry.</p></div>
  <div class="abs meal-row" style="top:834px"><div class="meal-thumb" role="img" aria-label="Fresh tomatoes" style="background:radial-gradient(circle,#e2473a,#9a2a20)"></div><p class="meal-text">Lorem Ipsum is simply dummy text of the printing and typesetting industry.</p></div>

  <div class="abs panel-photo" role="img" aria-label="Pantry staples: jars of grains, milk, eggs, honey, bread and vegetables" style="left:306px;top:702px;width:141px;height:118px;background:linear-gradient(160deg,#c8a070,#e8d8bc 50%,#b06a3a)"></div>
  <p class="abs panel-text">Lorem Ipsum is simply dummy text of the printing and typesetting industry. Lorem Ipsum has been the industry's standard dummy text ever since the 1500s, when an unknown printer took a galley of type and scrambled it to make a type specimen book.</p>

  <ul class="abs tips">
    <li>Eat healthy</li>
    <li>Lose weight</li>
    <li>Paleo diet</li>
    <li>What to eat</li>
    <li>What to buy</li>
  </ul>
  <div class="abs panel-photo" role="img" aria-label="Ripe tomatoes with garlic bulbs" style="left:490px;top:798px;width:140px;height:72px;background:linear-gradient(120deg,#e9e4dc 0%,#d0443a 45%,#b52a20 100%)"></div>

  <div class="abs view-btn" style="left:165px">VIEW MORE</div>
  <div class="abs view-btn" style="left:347px">VIEW MORE</div>
  <div class="abs view-btn" style="left:529px">VIEW MORE</div>

  <!-- newsletter & follow -->
  <h3 class="abs section-label" style="left:114px;top:924px">Newsletter signup</h3>
  <div class="abs email-field">Your Email Here</div>
  <div class="abs submit-btn">SUBMIT</div>

  <h3 class="abs section-label" style="left:385px;top:935px">Follow us and get to know us better</h3>
  <div class="abs follow-row">
    <span class="ring"></span><span class="chip">Follow</span><span class="chip">30.9K followers</span>
    <span class="gap"></span>
    <span class="ring"></span><span class="chip dark">Like</span><span class="chip">713k</span>
    <span class="gap"></span>
    <span class="ring"></span><span class="sq"></span>
  </div>

  <!-- footer -->
  <div class="abs footer"></div>
  <div class="abs foot-col" style="left:114px;width:106px">
    <h3>Get started</h3>
    <ul><li>How it Works</li><li>Our Pricing</li><li>Why Us?</li></ul>
  </div>
  <div class="abs foot-col" style="left:238px;width:106px">
    <h3>Help</h3>
    <ul><li>FAQ's</li><li>Packing Tips</li><li>Contact us</li></ul>
  </div>
  <div class="abs foot-col" style="left:362px;width:106px">
    <h3>Company</h3>
    <ul><li>About Us</li><li>Services</li><li>Blog Posts</li></ul>
  </div>
  <div class="abs foot-col contact" style="left:485px;width:155px">
    <h3>Get in touch</h3>
  </div>
  <div class="abs foot-icon" style="left:487px"></div>
  <div class="abs foot-icon" style="left:518px"></div>
  <div class="abs foot-icon" style="left:549px"></div>
  <div class="abs foot-icon" style="left:581px"></div>

  <div class="abs foot-brand">Harvest Table Menus</div>
  <div class="abs copyright">Copyright 2014 © Harvest Table Menus. - All Rights Reserved</div>

</div>
</body>
</html>
```